Commercial/Corporate Law Firm needs Website Design

Hi guys. I've started up a new law firm and would love your help designing an attractive website. I'll need both design and coding, and to make it easy for us to edit as necessary later, I think it should be built off a Wordpress.org structure.
FIRST IMPRESSIONS
It's very important that the first impression of the website really captures our prospective clients' attention and impresses them. Their first three seconds needs to be good.
I imagine the homepage may be short, with a menu bar and a compelling image, and with a tagline overlaid or underneath (eg. "It's about results.")
The image should be related to our practice areas: eg. IPOs, corporate transactions, or commercial negotiations.
I have previously suggested there could be a skyline image of Sydney or Adelaide. However, because we are based in Adelaide, I don't think Sydney is appropriate - and Adelaide is probably too boring to use.
HOMEPAGE
Being a new firm, we don't have many existing testimonials, and I will be the only lawyer to start with. So we need to focus on the nature of the services we will provide and how my experience can help them. We have an existing logo to use, and I would like the website colour scheme not to clash with that logo (dark blue and white).
After the initial image and tagline there should be a brief introduction to each of the main areas of work, eg. "We specialise in three main areas of practice:"
1. Corporate Transactions and Regulation
2. Business Law and Dispute Resolution
3. Migration Assistance
These should each have an appropriate photo and link to a separate page that briefly describes our services in that area.
Below that there should be a message from me with a photo. Finally, at the bottom, there should be a "Contact Us" section which shows a Google image of our address, contact details, and then our logo with colours inverted.
OTHER PAGES
While we will need some other pages, they should all be fairly simple. I think we will need one page to say "About Us", where I will put information about my experience. I think we will then need one page for each of the 3 areas listed above, which just needs an appropriate image and then text to describe the service. Finally, a "Contact Us" page which I imagine will be the same as the bottom of the homepage.
OTHER DETAILS
For now you can use details from my LinkedIn page to fill out any other text as necessary, or the photo.
Because the logo is square, I would prefer the design of the website also to be rectangular.
Looking forward to seeing your work! Thank you.
Good luck,
Marcus
Target Market(s)
Potential clients:
Businesses with legal issues or disputes
Companies wishing to list on the stock market

```html
<!DOCTYPE html>
<html lang="en">
<head>
<meta charset="utf-8">
<title>Corvane Legal</title>
<link rel="stylesheet" href="https://fonts.googleapis.com/css2?family=Lato:wght@400;700&family=Lora:wght@400;500&display=swap">
<style>
:root{
  --navy:#1b3563;
  --navy-deep:#12254a;
  --accent:#2f6cc4;
  --ink:#3d4350;
  --muted:#5c6270;
  --rule:#c9ccd2;
  --topbar:#f4f4f4;
  --white:#ffffff;
}
*{box-sizing:border-box;margin:0;padding:0}
html,body{width:1200px;height:2258px;overflow:hidden;background:var(--white)}
body{font-family:"Lato",Arial,sans-serif;color:var(--ink);position:relative}
.serif{font-family:"Lora",Georgia,serif}
a{color:inherit;text-decoration:none}

/* top bar */
.topbar{position:absolute;top:0;left:0;width:1200px;height:38px;background:var(--topbar)}
.topbar-contacts{position:absolute;right:240px;top:0;height:38px;display:flex;align-items:center;gap:26px;font-size:11px;color:var(--ink)}
.topbar-contacts span{display:flex;align-items:center;gap:9px}
.topbar-contacts svg{width:11px;height:11px;fill:var(--navy)}

/* logo badge */
.brand-badge{position:absolute;left:241px;top:0;width:165px;height:118px;z-index:3}
.brand-badge svg.badge-shape{position:absolute;inset:0}
.brand-name{position:absolute;left:0;right:0;top:18px;text-align:center;font-family:"Lora",Georgia,serif;font-weight:400;color:var(--navy);font-size:17px;letter-spacing:2px;line-height:20px;text-transform:uppercase}
.brand-mark{display:block;width:22px;height:22px;background:var(--navy);margin:0 auto 8px}

/* hero */
.hero{position:absolute;top:38px;left:0;width:1200px;height:474px;background:
  radial-gradient(ellipse at 52% 30%,rgba(176,104,72,.55) 0%,rgba(176,104,72,0) 38%),
  linear-gradient(100deg,#1d2c45 0%,#223552 40%,#2a3a55 60%,#15233b 100%)}
.main-nav{position:absolute;top:24px;right:240px;display:flex;gap:25px;font-size:10.5px;font-weight:700;letter-spacing:.3px;color:var(--white);text-transform:uppercase}
.hero-title{position:absolute;left:241px;top:262px;font-family:"Lora",Georgia,serif;font-weight:400;font-size:50px;line-height:49px;color:var(--white)}
.social{position:absolute;left:883px;top:396px;display:flex;gap:15px}
.social i{display:block;width:9px;height:9px;border-radius:50%;background:var(--white)}

/* section headings */
.section-head{position:absolute;left:241px;width:719px;display:flex;align-items:center;gap:18px}
.section-head::before,.section-head::after{content:"";flex:1;height:1px;background:var(--rule)}
.section-head h2{font-family:"Lora",Georgia,serif;font-weight:400;color:var(--navy);font-size:25px;line-height:25px;text-align:center}

/* practice cards */
.practice-head{top:574px}
.practice-grid{position:absolute;left:241px;top:661px;width:719px;display:flex;gap:19px}
.practice-card{position:relative;width:227px;height:353px;background:var(--white);box-shadow:0 2px 6px rgba(0,0,0,.12);text-align:center}
.practice-photo{height:172px}
.photo-contract{background:linear-gradient(135deg,#c9d3de 0%,#e9edf1 55%,#b8c2cf 100%)}
.photo-handshake{background:linear-gradient(135deg,#7c8796 0%,#c9ad92 50%,#b7a28c 100%)}
.photo-passport{background:linear-gradient(135deg,#2a2e38 0%,#3a4a74 45%,#c9a77b 100%)}
.practice-card h3{font-family:"Lora",Georgia,serif;font-weight:400;color:var(--navy);font-size:18px;line-height:21px;margin-top:21px;height:44px}
.practice-card p{font-size:10.5px;line-height:15.5px;color:var(--muted);padding:0 28px;margin-top:7px}
.btn{display:inline-flex;align-items:center;justify-content:center;gap:7px;height:38px;background:var(--navy);color:var(--white);font-size:9.5px;font-weight:700;letter-spacing:.3px;text-transform:uppercase}
.btn svg{width:5px;height:7px;fill:currentColor}
.practice-card .btn{position:absolute;left:57px;top:333px;width:122px}

/* lawyer's desk */
.desk{position:absolute;top:1114px;left:0;width:1200px;height:467px;background:var(--navy)}
.desk-backdrop{position:absolute;left:0;top:0;width:406px;height:467px;background:linear-gradient(180deg,#eceeef 0%,#d3d6da 55%,#a9aeb5 100%)}
.desk-portrait{position:absolute;left:241px;top:60px;width:346px;height:407px;background:linear-gradient(180deg,#d7b8a2 0%,#c09a82 30%,#2c3346 45%,#232a3b 100%)}
.desk-copy{position:absolute;left:610px;top:60px;width:352px;color:var(--white)}
.desk-copy h2{font-family:"Lora",Georgia,serif;font-weight:400;font-size:24px;line-height:30px;margin-bottom:22px}
.desk-copy p{font-size:10.4px;line-height:15px;margin-bottom:13px}
.desk-copy .btn{background:var(--accent);width:123px;margin-top:16px}

/* contact */
.contact-head{top:1643px}
.contact-map{position:absolute;left:241px;top:1719px;width:473px;height:283px;background:linear-gradient(120deg,#a9cdeb 0%,#a9cdeb 9%,#eef0e8 11%,#e9ece3 55%,#cfe3c6 80%,#eef0e8 100%)}
.contact-list{position:absolute;left:732px;top:1722px;width:228px;list-style:none;font-size:10.5px;line-height:15px;color:var(--ink)}
.contact-list li{display:flex;gap:17px;border-bottom:1px solid #e2e4e8}
.contact-list li:nth-child(1){padding-bottom:21px}
.contact-list li:nth-child(2),.contact-list li:nth-child(3){padding:14px 0 15px}
.contact-list li:last-child{border-bottom:none;padding-top:14px}
.contact-list svg{width:10px;height:11px;fill:var(--navy);flex:none;margin-top:2px}

/* footer */
.site-footer{position:absolute;top:2067px;left:0;width:1200px;height:191px;background:var(--navy);color:var(--white)}
.footer-brand{position:absolute;left:263px;top:38px;width:120px;text-align:center;font-family:"Lora",Georgia,serif;font-weight:400;font-size:17px;letter-spacing:2px;line-height:20px;text-transform:uppercase;color:var(--white)}
.footer-brand .brand-mark{background:var(--white)}
.footer-nav{position:absolute;right:240px;top:65px;display:flex;gap:25px;font-size:10.5px;font-weight:700;letter-spacing:.3px;text-transform:uppercase}
.footer-rule{position:absolute;left:241px;top:143px;width:719px;height:1px;background:#34508a}
.copyright{position:absolute;left:0;width:1200px;top:160px;text-align:center;font-size:10px}
</style>
</head>
<body>

<header class="topbar">
  <div class="topbar-contacts">
    <span><svg viewBox="0 0 12 10"><path d="M0 0h12v10H0z M1 1.2v.4l5 3.4 5-3.4v-.4z" fill-rule="evenodd"/></svg>legal@corvanelegal.com.au</span>
    <span><svg viewBox="0 0 12 12"><path d="M2.5 0l2 2.6-1.2 1.6c.8 1.7 2.2 3.1 3.9 3.9l1.6-1.2L12 9.5 10.6 12C5 11.6.4 7 0 1.4z"/></svg>+61 8 5550 1924</span>
  </div>
</header>

<div class="brand-badge">
  <svg class="badge-shape" viewBox="0 0 165 118" width="165" height="118"><path d="M0 0h165v100l-82.5 18L0 100z" fill="#ffffff"/></svg>
  <div class="brand-name"><span class="brand-mark"></span>Corvane<br>Legal</div>
</div>

<section class="hero" role="img" aria-label="Photo of two business people shaking hands over a city harbour skyline at dusk">
  <nav class="main-nav"><a>Home</a><a>About Us</a><a>Services</a><a>Case Studies</a><a>Contact Us</a></nav>
  <h1 class="hero-title">We<br>Get<br>Results.</h1>
  <div class="social"><i></i><i></i><i></i></div>
</section>

<div class="section-head practice-head"><h2>We specialise in<br>three main areas of practice</h2></div>

<section class="practice-grid">
  <article class="practice-card">
    <div class="practice-photo photo-contract" role="img" aria-label="Photo of a hand signing a contract"></div>
    <h3>Corporate Transactions<br>and Regulation</h3>
    <p>Mel ei postea singulis erroribus. Usu te odio delenit. Nec id paulo mandamus hendrerit, vis ne liber nonumy fierent.</p>
    <a class="btn">Learn More <svg viewBox="0 0 5 7"><path d="M0 0l5 3.5L0 7z"/></svg></a>
  </article>
  <article class="practice-card">
    <div class="practice-photo photo-handshake" role="img" aria-label="Photo of a business handshake over documents"></div>
    <h3>Business Law and<br>Dispute Resolution</h3>
    <p>Mel ei postea singulis erroribus. Usu te odio delenit. Nec id paulo mandamus hendrerit, vis ne liber nonumy fierent.</p>
    <a class="btn">Learn More <svg viewBox="0 0 5 7"><path d="M0 0l5 3.5L0 7z"/></svg></a>
  </article>
  <article class="practice-card">
    <div class="practice-photo photo-passport" role="img" aria-label="Photo of a gloved hand presenting a passport across a desk"></div>
    <h3>Migration Assistance</h3>
    <p>Mel ei postea singulis erroribus. Usu te odio delenit. Nec id paulo mandamus hendrerit, vis ne liber nonumy fierent.</p>
    <a class="btn">Learn More <svg viewBox="0 0 5 7"><path d="M0 0l5 3.5L0 7z"/></svg></a>
  </article>
</section>

<section class="desk">
  <div class="desk-backdrop" role="img" aria-label="Faded photo of a city waterfront at night"></div>
  <div class="desk-portrait" role="img" aria-label="Portrait photo of the lawyer in a dark suit and red tie"></div>
  <div class="desk-copy">
    <h2>From The Lawyer’s Desk</h2>
    <p>Marcus’s rare regulatory experience in public fundraisings and mergers and acquisitions is a compelling advantage for any company seeking to complete a significant transaction quickly.</p>
    <p>Marcus assisted draft NCRA’s regulatory guidance on prospectuses. With his team Marcus was awarded a National Service Achievement Medal, “ reserved for the highest level of recognition”, and awarded “to recognise the significant contribution made to the nation by individuals in the public service”.</p>
    <p>Marcus guides corporate transactions through the regulatory hurdles to help minimise the chance of failure and delay, and maximise your chance of success.</p>
    <a class="btn">Learn More <svg viewBox="0 0 5 7"><path d="M0 0l5 3.5L0 7z"/></svg></a>
  </div>
</section>

<div class="section-head contact-head"><h2>Contact Us</h2></div>

<div class="contact-map" role="img" aria-label="Street map of the city showing the office location"></div>

<ul class="contact-list">
  <li><svg viewBox="0 0 10 12"><path d="M5 0a4 4 0 0 1 4 4c0 3-4 8-4 8S1 7 1 4a4 4 0 0 1 4-4zm0 2.4A1.6 1.6 0 1 0 5 5.6 1.6 1.6 0 0 0 5 2.4z" fill-rule="evenodd"/></svg><span>4th Floor, 17 Harlow Street,<br>Adelaide, South Australia 5000,<br>Australia</span></li>
  <li><svg viewBox="0 0 12 12"><path d="M2.5 0l2 2.6-1.2 1.6c.8 1.7 2.2 3.1 3.9 3.9l1.6-1.2L12 9.5 10.6 12C5 11.6.4 7 0 1.4z"/></svg><span>+61 8 5550 1924</span></li>
  <li><svg viewBox="0 0 12 12"><path d="M3 0h6v3H3zM0 4h12v6h-2V8H2v2H0zM3 9h6v3H3z"/></svg><span>+61 8 5550 1925</span></li>
  <li><svg viewBox="0 0 12 10"><path d="M0 0h12v10H0z M1 1.2v.4l5 3.4 5-3.4v-.4z" fill-rule="evenodd"/></svg><span>legal@marcuscorvane.com</span></li>
</ul>

<footer class="site-footer">
  <div class="footer-brand"><span class="brand-mark"></span>Corvane<br>Legal</div>
  <nav class="footer-nav"><a>Home</a><a>About Us</a><a>Services</a><a>Case Studies</a><a>Contact Us</a></nav>
  <div class="footer-rule"></div>
  <p class="copyright">Copyright © 2018 Corvane Legal</p>
</footer>

</body>
</html>
```